Modern brochure by Lawyers, for modern clients

It'sa "News" for their clients. Attached you can find the current News without design. It must be elegant but very attractive and modern. Their web site is http://www.montealtoyasociados.cl/ Their expertise is labor and employment practice area. It must be in editable format so that lawyers can write the news in a template with this corporate design.

Target Market(s)

Big Companies

Font styles to use
Sans Serif

Colors
0255a3
474747

Requirements
Nice to have
• Legal Pictures and only a little of yellow. One touch! It must be in editable format so that lawyers can write the news in a template with this corporate design.

```html
<!DOCTYPE html>
<html lang="es">
<head>
<meta charset="utf-8">
<title>Montealto &amp; Asociados — Noticias</title>
<link href="https://fonts.googleapis.com/css2?family=Lato:wght@300;400;700;900&display=swap" rel="stylesheet">
<style>
  :root {
    --backdrop: #e6e6e3;
    --paper: #ffffff;
    --navy: #3d5576;
    --navy-dark: #3a4f6e;
    --sky-light: #3f70c8;
    --sky-deep: #2c53ab;
    --steel: #8fa3ad;
    --mist: #cbd9e0;
    --frost: #e4eef2;
    --ink: #2f353d;
    --ink-strong: #111418;
    --link: #2b4a7a;
  }
  * { box-sizing: border-box; margin: 0; padding: 0; }
  html, body { width: 1200px; height: 1200px; overflow: hidden; }
  body {
    background: var(--backdrop);
    font-family: "Lato", sans-serif;
    position: relative;
  }
  .newsletter {
    position: absolute;
    left: 176px; top: 0;
    width: 848px; height: 1200px;
    background: var(--paper);
    overflow: hidden;
  }
  .newsletter__art {
    position: absolute; left: 0; top: 0;
    width: 848px; height: 1200px;
  }
  .brand {
    position: absolute; left: 46px; top: 78px;
    display: flex; align-items: center; gap: 14px;
  }
  .brand__dot {
    width: 58px; height: 58px; border-radius: 50%;
    background: var(--navy);
  }
  .brand__name {
    font-weight: 300; color: var(--navy);
    font-size: 40px; line-height: 1; letter-spacing: 1.5px;
    text-transform: uppercase;
  }
  .brand__name span { display: block; font-size: 28px; letter-spacing: 1px; margin-top: 2px; }
  .brand__rule {
    position: absolute; left: 470px; top: 63px;
    width: 5px; height: 81px;
    background: linear-gradient(to bottom, var(--frost) 0 30%, var(--steel) 30% 70%, var(--navy) 70% 100%);
  }
  .issue-date {
    position: absolute; right: 54px; top: 118px;
    font-size: 19px; font-weight: 300; color: var(--navy);
  }
  .hero-title {
    position: absolute; left: 54px; top: 286px;
    color: #fff;
  }
  .hero-title__main { font-weight: 900; font-size: 56px; line-height: 1; letter-spacing: -0.5px; }
  .hero-title__sub { font-weight: 300; font-size: 23px; letter-spacing: 0.3px; margin-top: 2px; }
  .letter {
    position: absolute; left: 97px; top: 694px; width: 660px;
    font-size: 15.4px; font-weight: 300; line-height: 19px; color: var(--ink);
  }
  .letter p { margin-bottom: 18px; text-align: justify; }
  .letter .greeting { margin-bottom: 9px; }
  .letter .cta { font-weight: 700; color: var(--ink-strong); text-align: left; margin-bottom: 11px; }
  .letter .cta a { color: var(--link); text-decoration: underline; }
  .letter .closing { margin-bottom: 10px; }
  .letter .signature { font-weight: 400; color: var(--ink-strong); }
  .contact-bar {
    position: absolute; left: 0; bottom: 0; width: 848px; height: 34px;
    background: var(--navy-dark); color: #fff;
    display: flex; align-items: center; justify-content: center; gap: 20px;
    font-size: 12.3px; font-weight: 400;
  }
</style>
</head>
<body>
<main class="newsletter">
  <svg class="newsletter__art" viewBox="0 0 964 1364" preserveAspectRatio="none">
    <defs>
      <linearGradient id="skyFill" x1="0" y1="0" x2="1" y2="1">
        <stop offset="0" stop-color="var(--sky-light)"/>
        <stop offset="1" stop-color="var(--sky-deep)"/>
      </linearGradient>
      <linearGradient id="accentFill" x1="0" y1="0" x2="1" y2="0">
        <stop offset="0" stop-color="var(--frost)" stop-opacity="0"/>
        <stop offset="0.5" stop-color="var(--mist)"/>
        <stop offset="1" stop-color="var(--steel)"/>
      </linearGradient>
    </defs>
    <g role="img" aria-label="Fotografía de un edificio corporativo de vidrio azul contra el cielo">
      <polygon points="0,200 964,200 964,530 0,785" fill="url(#skyFill)"/>
    </g>
    <rect class="hero-edge" x="0" y="0" width="0" height="0"/>
    <polygon points="0,787 964,532 964,544 0,798" fill="var(--mist)"/>
    <g role="img" aria-label="Gráfica decorativa en tonos azul grisáceo">
      <polygon points="430,700 964,552 964,789" fill="url(#accentFill)"/>
    </g>
  </svg>

  <header>
    <div class="brand">
      <div class="brand__dot"></div>
      <div class="brand__name">Montealto<span>&amp; Asociados</span></div>
    </div>
    <div class="brand__rule"></div>
    <p class="issue-date">Santiago, 25 de julio de 2018</p>
  </header>

  <div class="hero-title">
    <div class="hero-title__main">MONTEALTO</div>
    <div class="hero-title__sub">ASOCIADOS ABOGADOS</div>
  </div>

  <article class="letter">
    <p class="greeting">Estimados,</p>
    <p>Por medio del presente, les damos a conocer el Dictamen Ordinario N° 3826-031, emitido por la Dirección del Trabajo el pasado 20 de julio, relativo a los “beneficios históricos”.</p>
    <p>Estos fueron definidos en su oportunidad por este organismo como “…aquellos beneficios que se han otorgado desde siempre…” por parte del empleador.</p>
    <p>A partir de este Dictamen, el cual reconsidera el criterio del anterior Director del Trabajo, los beneficios históricos vuelven a ser patrimonio de la empresa y de los trabajadores que los han recibido, dejando de serlo de la organización sindical y de sus socios beneficiados por el solo hecho de haberse “replicado” en un instrumento colectivo durante una negociación.</p>
    <p>Por último, el Dictamen en comento aclara que si un “beneficio histórico” se incrementa de manera real y efectiva producto de una negociación colectiva, únicamente dicho incremento se entenderá originado en el respectivo instrumento colectivo, y en consecuencia, objeto de una posible extensión en el evento de que ésta se haya acordado durante la negociación.</p>
    <p class="cta">Para mayor análisis de lo resuelto por la Dirección del Trabajo, se puede revisar el Dictámen en comento <a href="http://www.montealtoyasociados.cl/">haciendo click aquí</a></p>
    <p class="closing">Sin otro particular, saluda atentamente a ustedes,</p>
    <p class="signature">Montealto &amp; Asociados<br>oficina@montealtoyasociados.cl</p>
  </article>

  <footer class="contact-bar">
    <span>Av. Los Alerces 2140, piso 3, Providencia</span>
    <span>T +56 2 2345 6789</span>
    <span>E oficina@montealtoyasociados.cl</span>
    <span>www.montealtoyasociados.cl</span>
  </footer>
</main>
</body>
</html>
```